Organic All Natural Gluten Free Dog Treat company needs a Design for our Label/Packaging.

We are a start up company making organic all natural gluten free dog biscuits. We are looking for a catchy label design that will impress upon first sight. Colors can be almost anything, some to consider are green, blue, white, beige, Black, Burgundy. We will be running a high class, high end business and really need to see concepts that reflect this. We are not really looking for anything comical or fun, however it needs to be nice to look at and look to be high end quality. The photo's that I have attached are what we like from other companies, these are just to throw around and maybe get ideas from. Our labels will be either 4" wide x 5" high or 5" wide x 6" high.
Updates

Project Deadline Extended Reason: We wish to extend 5 days as we would like to see more designs. Added Tuesday, July 7, 2015

Project Deadline Extended
Reason: Need more designs to make final decision.

Target Market(s)

Anyone who owns dog's or dog lover's.

Industry/Entity Type

It Company

Font styles to use
Serif
Sans Serif
Decorative
Script

Requirements
Must have
• "Stay Close Alwaystime" is the name of our business so it needs to be included,
• All Natural Organic Dog Treats...Gluten Free, No Preservatives, No Wheat, No Soy, Corn, or GMO's, Nothing Artificial, Baked by Stay Close AlwaysTime LLC., Dallas, TX.
• 6 oz., made in U.S.A.
• We don't need to use the logo, as long as the words "Stay Close AlwaysTime" are included.
Nice to have
• Not sure what colors we want, we would like to see a variety which can include brown, blue, black, green, red, yellow, orange, purple, beige, burgundy, white color scheme?? Maybe white or brownish, blueish background? American flag.
• We have uploaded a photo tilted American Eskimo Puppies for Label, we would like to have this included if possible. We have 4 flavors, Peanut Butter N' Honey, Pumpkin N' Spice, Sweet Potato, and Blueberry N' Coconut, maybe you can add the name and color code for one of these.

```html
<!DOCTYPE html>
<html lang="en">
<head>
<meta charset="utf-8">
<title>Stay Close Alwaystime – Dog Treat Label</title>
<link rel="stylesheet" href="https://fonts.googleapis.com/css2?family=Oswald:wght@700&family=Arimo:wght@400;700&family=Tinos:wght@700&display=swap">
<style>
  :root {
    --page: #f5f5f5;
    --brown-light: #9c6a4c;
    --brown-dark: #6b432d;
    --grass-light: #7cb342;
    --grass-dark: #3c7a22;
    --forest: #0f5a2c;
    --frame-green: #1f6b3a;
    --treat-brown: #7a4a2c;
    --ribbon-brown: #8a5a3c;
    --check-green: #1d5a2e;
    --badge-yellow: #f4e51c;
    --white: #ffffff;
    --ink: #2a1a10;
  }
  html, body {
    margin: 0;
    width: 1200px;
    height: 972px;
    overflow: hidden;
    background: var(--page);
  }
  .label {
    position: absolute;
    left: 320px;
    top: 126px;
    width: 560px;
    height: 720px;
    background: linear-gradient(135deg, var(--brown-light), var(--brown-dark));
    overflow: hidden;
    box-shadow: 0 2px 8px rgba(0,0,0,0.15);
  }
  .brand-name {
    position: absolute;
    top: 120px;
    left: 0;
    width: 100%;
    margin: 0;
    text-align: center;
    font-family: "Oswald", sans-serif;
    font-weight: 700;
    font-size: 58px;
    line-height: 1.05;
    letter-spacing: 2px;
    color: var(--white);
    text-transform: uppercase;
  }
  .photo-scene {
    position: absolute;
    left: 0;
    top: 0;
    width: 560px;
    height: 720px;
  }
  .treat-window {
    position: absolute;
    left: 432px;
    top: 372px;
    width: 96px;
    height: 220px;
    background: var(--frame-green);
    padding: 8px;
    box-sizing: border-box;
  }
  .treat-window .treat-photo {
    width: 100%;
    height: 100%;
    background: linear-gradient(160deg, #8d5a36, var(--treat-brown) 60%, #5e3820);
  }
  .free-badge {
    position: absolute;
    left: 36px;
    top: 318px;
    width: 126px;
    padding: 6px 0 4px;
    background: var(--frame-green);
    border: 2px solid var(--white);
    border-radius: 4px;
    transform: rotate(-16deg);
    text-align: center;
    font-family: "Arimo", sans-serif;
    font-weight: 700;
    color: var(--badge-yellow);
    line-height: 1;
  }
  .free-badge .badge-top { font-size: 13px; display: block; }
  .free-badge .badge-main { font-size: 26px; display: block; }
  .claims {
    position: absolute;
    left: 262px;
    top: 470px;
    width: 156px;
    margin: 0;
    padding: 0;
    list-style: none;
    font-family: "Arimo", sans-serif;
    font-size: 16px;
    color: var(--check-green);
    line-height: 20px;
    white-space: nowrap;
  }
  .claims li { display: flex; align-items: center; gap: 7px; }
  .claims svg { width: 13px; height: 13px; flex: none; }
  .product-ribbon {
    position: absolute;
    left: 132px;
    top: 574px;
    width: 286px;
    height: 28px;
    background: var(--ribbon-brown);
    border-radius: 3px;
    font-family: "Tinos", serif;
    font-weight: 700;
    font-size: 17px;
    line-height: 28px;
    text-align: center;
    color: var(--ink);
  }
  .footer-band {
    position: absolute;
    left: 0;
    top: 636px;
    width: 100%;
    height: 84px;
    background: var(--forest);
    border-top: 3px solid var(--white);
    font-family: "Arimo", sans-serif;
    color: var(--white);
  }
  .net-weight {
    position: absolute;
    right: 24px;
    top: 16px;
    font-family: "Tinos", serif;
    font-weight: 700;
    font-size: 20px;
  }
  .baker {
    position: absolute;
    right: 24px;
    top: 46px;
    font-size: 11px;
  }
</style>
</head>
<body>
  <section class="label">
    <svg class="photo-scene" viewBox="0 0 560 720" role="img" aria-label="Photo of a white puppy running across green grass">
      <defs>
        <linearGradient id="grass" x1="0" y1="0" x2="0" y2="1">
          <stop offset="0" stop-color="var(--grass-light)"/>
          <stop offset="1" stop-color="var(--grass-dark)"/>
        </linearGradient>
      </defs>
      <path d="M0,420 Q280,340 560,410 L560,720 L0,720 Z" fill="url(#grass)" stroke="var(--white)" stroke-width="3"/>
    </svg>

    <h1 class="brand-name">Stay Close<br>Alwaystime</h1>

    <div class="free-badge">
      <span class="badge-top">Grain &amp; Gluten</span>
      <span class="badge-main">Free</span>
    </div>

    <div class="treat-window">
      <div class="treat-photo" role="img" aria-label="Photo of baked dog treats"></div>
    </div>

    <ul class="claims">
      <li><svg viewBox="0 0 13 13"><rect x="0.5" y="0.5" width="12" height="12" fill="var(--check-green)"/><path d="M3 6.5 L5.5 9 L10 3.5" fill="none" stroke="var(--white)" stroke-width="1.8"/></svg>No Soy</li>
      <li><svg viewBox="0 0 13 13"><rect x="0.5" y="0.5" width="12" height="12" fill="var(--check-green)"/><path d="M3 6.5 L5.5 9 L10 3.5" fill="none" stroke="var(--white)" stroke-width="1.8"/></svg>No Corn</li>
      <li><svg viewBox="0 0 13 13"><rect x="0.5" y="0.5" width="12" height="12" fill="var(--check-green)"/><path d="M3 6.5 L5.5 9 L10 3.5" fill="none" stroke="var(--white)" stroke-width="1.8"/></svg>No GMO's</li>
      <li><svg viewBox="0 0 13 13"><rect x="0.5" y="0.5" width="12" height="12" fill="var(--check-green)"/><path d="M3 6.5 L5.5 9 L10 3.5" fill="none" stroke="var(--white)" stroke-width="1.8"/></svg>No Preservatives</li>
    </ul>

    <div class="product-ribbon">All Natural Organic Dog Treats</div>

    <footer class="footer-band">
      <span class="net-weight">Net. Wt : 1 kg</span>
      <span class="baker">Baked by Stay Close AlwaysTime LLC.</span>
    </footer>
  </section>
</body>
</html>
```